Website header graphic

I'm looking for a professional website header graphic to be designed based on the attached mockup. I'm open to suggestions on the layout. Notes:
1. The text at the bottom should be graphical in some way. Each feature (CRM, etc.) in their individual clouds??? I'll leave it to your creative skills. :)
2. The van needs to have a wrap design that does NOT have a company name, but has the words HVAC, Plumbing, Electrical and look like a real work van.
3. Need to include a 25 year badge. Does not have to be like the one in the mockup. Just added that for reference. Just needs a design that works with the rest of the graphic.
4. I do need the final deliverable in a PSD layered file in 300dpi
5. End result must be realistic clouds, van, etc. with a professional look. Not looking for a cartoon or kids style illustration.
Thank you, Gordon

```html
<!DOCTYPE html>
<html lang="en">
<head>
<meta charset="utf-8">
<title>Grow Your Business on the Cloud</title>
<link href="https://fonts.googleapis.com/css2?family=Montserrat:ital,wght@0,300;0,600;0,700;1,300;1,500;1,900&family=Anton&display=swap" rel="stylesheet">
<style>
  :root {
    --stage: #9a9ba0;
    --sky-deep: #00367c;
    --sky-mid: #0b6cbf;
    --sky-light: #cfe5f6;
    --cloud: #ffffff;
    --ink-white: #ffffff;
    --accent-red: #e8141c;
    --label-grey: #767b84;
    --icon-blue: #1a3f93;
    --silver-hi: #f4f4f4;
    --silver-lo: #a9a9ab;
  }
  * { margin: 0; padding: 0; box-sizing: border-box; }
  html, body { width: 1200px; height: 612px; overflow: hidden; }
  body { background: var(--stage); font-family: "Montserrat", sans-serif; position: relative; }

  .header-banner {
    position: absolute; left: 0; top: 86px; width: 1200px; height: 440px; overflow: hidden;
    background:
      radial-gradient(ellipse 320px 90px at 170px 420px, rgba(255,255,255,.95), transparent 70%),
      radial-gradient(ellipse 420px 120px at 600px 430px, rgba(255,255,255,.95), transparent 70%),
      radial-gradient(ellipse 300px 110px at 1080px 380px, rgba(255,255,255,.9), transparent 70%),
      radial-gradient(ellipse 260px 80px at 420px 300px, rgba(255,255,255,.7), transparent 70%),
      linear-gradient(180deg, var(--sky-deep) 0%, var(--sky-mid) 42%, var(--sky-light) 66%, var(--cloud) 90%);
  }

  .headline {
    position: absolute; left: 48px; top: 22px;
    color: var(--ink-white); font-weight: 900; font-style: italic;
    font-size: 47px; line-height: 60px; letter-spacing: .5px;
    text-shadow: 2px 3px 0 #0d3f8f;
  }
  .tagline {
    position: absolute; left: 48px; top: 215px; width: 431px; height: 36px;
    background: var(--accent-red); transform: skewX(-12deg);
  }
  .tagline span {
    display: block; transform: skewX(12deg); color: var(--ink-white);
    font-style: italic; font-weight: 500; font-size: 16.5px; line-height: 36px; text-align: center;
  }

  .anniversary-number {
    position: absolute; left: 50px; top: 244px;
    font-weight: 900; font-style: italic; font-size: 170px; letter-spacing: -14px; line-height: 1;
    background: linear-gradient(160deg, var(--silver-hi) 15%, var(--silver-lo) 60%, #e2e2e2 85%);
    -webkit-background-clip: text; background-clip: text; color: transparent;
    filter: drop-shadow(3px 4px 3px rgba(0,0,0,.18));
  }
  .anniversary-words {
    position: absolute; left: 257px; top: 306px; color: #8d9096;
    font-weight: 300; font-style: italic; font-size: 29px; line-height: 33px;
    padding-bottom: 8px; border-bottom: 2px solid #b4b6ba; width: 176px; white-space: nowrap;
  }

  .service-van {
    position: absolute; left: 763px; top: 94px; width: 403px; height: 248px;
    border-radius: 40px 60px 24px 24px;
    background: linear-gradient(160deg, #ffffff 0%, #eceef0 55%, #8f9499 100%);
    box-shadow: 0 14px 20px rgba(60,80,110,.25);
  }
  .van-trades {
    position: absolute; left: 283px; top: 46px; color: var(--accent-red);
    font-family: "Anton", sans-serif; font-size: 27px; line-height: 30px; text-align: center;
    transform: rotate(3deg);
  }

  .feature-ring { position: absolute; left: 0; top: 0; }
  .feature-icon {
    position: absolute; width: 44px; height: 44px; border-radius: 50%;
    background: var(--cloud); box-shadow: 0 2px 6px rgba(0,40,100,.35);
    display: flex; align-items: center; justify-content: center; transform: translate(-50%,-50%);
  }
  .feature-icon svg { width: 24px; height: 24px; fill: none; stroke: var(--icon-blue); stroke-width: 1.5; stroke-linecap: round; stroke-linejoin: round; }
  .feature-label {
    position: absolute; transform: translate(-50%,-50%); white-space: nowrap;
    color: var(--label-grey); font-weight: 700; font-size: 15px;
  }
  .feature-label.on-sky { color: #c8d6e6; }
</style>
</head>
<body>
<section class="header-banner">
  <h1 class="headline">GROW<br>YOUR BUSINESS<br>ON THE CLOUD</h1>
  <div class="tagline"><span>TRUE All-In-One Services Business Software</span></div>

  <div class="anniversary-number">25</div>
  <div class="anniversary-words">Year<br>Anniversary</div>

  <svg class="feature-ring" width="1200" height="440" viewBox="0 0 1200 440" aria-hidden="true">
    <path d="M862 75 Q820 70 779 81 Q740 100 714 128 Q688 160 682 202 Q680 245 693 282 Q712 325 745 351 Q785 372 830 373 Q900 370 950 330"
          fill="none" stroke="#9fb4cc" stroke-width="1" stroke-dasharray="4 4"/>
  </svg>

  <div class="service-van" role="img" aria-label="Photo of a white work van with a trade wrap, floating on clouds">
    <div class="van-trades">HVAC<br>Plumbing<br>Electrical</div>
  </div>

  <span class="feature-label on-sky" style="left:753px;top:41px">Payroll</span>
  <div class="feature-icon" style="left:779px;top:81px"><svg viewBox="0 0 24 24"><circle cx="15" cy="8" r="4"/><path d="M15 6v4M3 15h4l4 2h6l3-2M3 19h14"/></svg></div>

  <span class="feature-label on-sky" style="left:862px;top:35px">CRM</span>
  <div class="feature-icon" style="left:862px;top:75px"><svg viewBox="0 0 24 24"><circle cx="12" cy="6" r="2.5"/><circle cx="6" cy="17" r="2.5"/><circle cx="18" cy="17" r="2.5"/><path d="M10 8l-3 7M14 8l3 7M8.5 17h7"/></svg></div>

  <span class="feature-label on-sky" style="left:636px;top:98px">Accounting</span>
  <div class="feature-icon" style="left:714px;top:128px"><svg viewBox="0 0 24 24"><rect x="4" y="3" width="13" height="17" rx="1"/><rect x="6.5" y="5.5" width="8" height="3"/><path d="M7 12h2M12 12h2M7 16h2M12 16h2"/></svg></div>

  <span class="feature-label on-sky" style="left:605px;top:200px">Inventory</span>
  <div class="feature-icon" style="left:682px;top:202px"><svg viewBox="0 0 24 24"><rect x="5" y="3" width="14" height="18" rx="1"/><path d="M8 8h2M12 8h4M8 12h2M12 12h4M8 16h2M12 16h4"/></svg></div>

  <span class="feature-label" style="left:620px;top:306px">Marketing</span>
  <div class="feature-icon" style="left:693px;top:282px"><svg viewBox="0 0 24 24"><path d="M4 10v4h3l8 5V5L7 10H4zM7 14l2 5M18 9l2-2M18 15l2 2M19 12h2"/></svg></div>

  <span class="feature-label" style="left:725px;top:394px">Dispatch</span>
  <div class="feature-icon" style="left:745px;top:351px"><svg viewBox="0 0 24 24"><path d="M6 3h9l4 4v14H6z"/><path d="M9 7h4v4H9zM9 14h7M9 17h7"/></svg></div>

  <span class="feature-label" style="left:830px;top:414px">Sales</span>
  <div class="feature-icon" style="left:830px;top:373px"><svg viewBox="0 0 24 24"><path d="M4 20l5-5 3 3 7-8M15 10h4v4"/></svg></div>
</section>
</body>
</html>
```